Bright Willow Wellness
Heal your Body Mind and Spirit
Bright Willow Wellness - Health
Creative Brief
Professional
Melora T. Grant, MA, CWC
Wellness Guide and Reflective Coach
Certifications: Feeling Map Form Key Spiritual Counseling
melora@brightwillowwellness.example
www.brightwillowwellness.example
Next appointment: _____________________________________
guest guest
where is the logo
mgrant417 mgrant417
Designers: Please only design for business cards, not stationary. Thanks...

```html
<!DOCTYPE html>
<html lang="en">
<head>
<meta charset="utf-8">
<title>Bright Willow Wellness – Business Card</title>
<link rel="stylesheet" href="https://fonts.googleapis.com/css2?family=Cinzel:wght@600&family=Lora:ital@1&family=Open+Sans:wght@400;600;700&display=swap">
<style>
  :root {
    --bg: #e9e6e1;
    --card: #ffffff;
    --navy: #1d4a73;
    --blue: #2b75a8;
    --blue-light: #6fa9d2;
    --ink: #2e2e2e;
    --muted: #6b6b6b;
    --rule: #9a9a9a;
  }
  * { margin: 0; padding: 0; box-sizing: border-box; }
  html, body { width: 1200px; height: 629px; overflow: hidden; }
  body {
    background: var(--bg);
    font-family: "Open Sans", Arial, sans-serif;
    color: var(--ink);
    position: relative;
  }
  .card {
    position: absolute;
    top: 166px;
    width: 520px;
    height: 297px;
    background: var(--card);
    box-shadow: 0 2px 10px rgba(0,0,0,.12);
    overflow: hidden;
  }
  .card--back { left: 53px; }
  .card--front { left: 627px; }

  /* Appointment side */
  .appt { padding: 34px 38px; }
  .appt__title { font-size: 15px; font-weight: 700; margin-bottom: 14px; }
  .appt__row { display: flex; align-items: flex-end; gap: 10px; font-size: 12px; margin-bottom: 16px; }
  .appt__line { flex: 1; border-bottom: 1px solid var(--rule); height: 14px; }
  .appt__days { display: flex; gap: 14px; margin: 6px 0 26px; font-size: 11px; font-weight: 600; }
  .appt__day { display: flex; align-items: center; gap: 5px; }
  .appt__box { width: 14px; height: 14px; border: 1px solid var(--ink); }
  .appt__policy-title { font-size: 12px; font-weight: 700; margin-bottom: 4px; }
  .appt__policy { font-size: 10px; color: var(--muted); }

  /* Brand side */
  .brand { position: absolute; left: 30px; top: 92px; display: flex; align-items: center; gap: 12px; }
  .brand__mark { width: 48px; height: 48px; border-radius: 50%; background: var(--navy); flex: none; }
  .brand__name { font-family: "Cinzel", Georgia, serif; font-weight: 600; font-size: 23px; color: var(--navy); letter-spacing: .5px; white-space: nowrap; }
  .brand__tagline { position: absolute; left: 92px; top: 140px; font-family: "Lora", Georgia, serif; font-style: italic; font-size: 13px; color: var(--navy); }

  .person { position: absolute; right: 26px; top: 196px; text-align: right; }
  .person__name { font-family: "Cinzel", Georgia, serif; font-weight: 600; font-size: 14px; color: var(--navy); white-space: nowrap; }
  .person__role { font-size: 9px; letter-spacing: 1px; text-transform: uppercase; color: var(--muted); line-height: 1.5; margin-top: 3px; }

  .contact-band { position: absolute; left: 0; bottom: 0; width: 12px; height: 86px; background: linear-gradient(var(--blue-light), var(--navy)); }
  .contact { position: absolute; left: 22px; bottom: 14px; list-style: none; font-size: 9.5px; color: var(--navy); }
  .contact__item { display: flex; align-items: center; gap: 6px; margin-top: 3px; white-space: nowrap; }
  .contact__icon { width: 13px; height: 13px; border-radius: 50%; background: var(--blue); display: flex; align-items: center; justify-content: center; flex: none; }
</style>
</head>
<body>
  <section class="card card--back" aria-label="Appointment side">
    <div class="appt">
      <h2 class="appt__title">Appointment</h2>
      <div class="appt__row"><span>Name</span><span class="appt__line"></span><span>Time</span><span class="appt__line"></span></div>
      <div class="appt__row"><span>Date</span><span class="appt__line"></span></div>
      <div class="appt__days">
        <span class="appt__day"><span class="appt__box"></span>MON</span>
        <span class="appt__day"><span class="appt__box"></span>TUE</span>
        <span class="appt__day"><span class="appt__box"></span>WED</span>
        <span class="appt__day"><span class="appt__box"></span>THU</span>
        <span class="appt__day"><span class="appt__box"></span>FRI</span>
        <span class="appt__day"><span class="appt__box"></span>SAT</span>
      </div>
      <h3 class="appt__policy-title">Cancellation Policy</h3>
      <p class="appt__policy">Please give 24 hours notice to cancel or a fee may apply.</p>
    </div>
  </section>

  <section class="card card--front" aria-label="Contact side">
    <div class="brand">
      <span class="brand__mark"></span>
      <span class="brand__name">BRIGHT WILLOW WELLNESS</span>
    </div>
    <p class="brand__tagline">steady care for body and spirit</p>

    <div class="person">
      <p class="person__name">Melora T. Grant, MA, CWC</p>
      <p class="person__role">Wellness Guide and<br>Reflective Coach</p>
    </div>

    <div class="contact-band"></div>
    <ul class="contact">
      <li class="contact__item">
        <span class="contact__icon"><svg width="8" height="8" viewBox="0 0 10 10"><path d="M2 1h2l1 2-1 1c.5 1 1.2 1.7 2 2l1-1 2 1v2c-4 0-7-3-7-7z" fill="#fff"/></svg></span>
        (555) 014-2290
      </li>
      <li class="contact__item">
        <span class="contact__icon"><svg width="8" height="8" viewBox="0 0 10 10"><rect x="1" y="2.5" width="8" height="5" fill="none" stroke="#fff"/><path d="M1 2.5l4 3 4-3" fill="none" stroke="#fff"/></svg></span>
        melora@brightwillowwellness.example
      </li>
      <li class="contact__item">
        <span class="contact__icon"><svg width="8" height="8" viewBox="0 0 10 10"><circle cx="5" cy="5" r="4" fill="none" stroke="#fff"/><path d="M1 5h8M5 1c2 2 2 6 0 8M5 1c-2 2-2 6 0 8" fill="none" stroke="#fff" stroke-width=".8"/></svg></span>
        www.brightwillowwellness.example
      </li>
      <li class="contact__item">
        <span class="contact__icon"><svg width="8" height="8" viewBox="0 0 10 10"><circle cx="5" cy="5" r="2.5" fill="#fff"/></svg></span>
        mgrant417
      </li>
    </ul>
  </section>
</body>
</html>
```